Business card for partnership

Plumbing and hvac company needing a minimal business card. We already have a logo i would like the front of the card just the logo and the back have all info.

Target Market(s)

Commercial facilities

Industry/Entity Type

Plumbing hvac

Contact Information for Business Card

We would like it double sided. Logo big and bold on the front and out info on the back. Our info on back would be name and position phone, email, and location

```html
<!DOCTYPE html>
<html lang="en">
<head>
<meta charset="utf-8">
<title>Anvil Mechanical – Business Card</title>
<link rel="stylesheet" href="https://fonts.googleapis.com/css2?family=Lato:wght@400;700;900&family=Oswald:wght@500&display=swap">
<style>
  :root {
    --backdrop: #1c1c1c;
    --card: #111111;
    --accent: #f08132;
    --ink: #ffffff;
    --rule: #8a8a8a;
  }
  * { box-sizing: border-box; margin: 0; padding: 0; }
  html, body {
    width: 1200px; height: 900px; overflow: hidden;
    background: var(--backdrop);
  }
  .sheet {
    position: relative; width: 1200px; height: 900px;
    display: flex; flex-direction: column; align-items: center;
    justify-content: center; gap: 48px;
  }
  .card {
    position: relative; width: 640px; height: 366px;
    background: var(--card);
    box-shadow: 0 10px 30px rgba(0,0,0,.55);
    overflow: hidden;
  }
  .card__band {
    position: absolute; left: 0; right: 0; bottom: 0; height: 11px;
    background: var(--accent);
  }
  /* front */
  .card--front { display: flex; align-items: center; justify-content: center; }
  .wordmark {
    font-family: 'Lato', sans-serif; font-weight: 900;
    color: var(--ink); text-align: center; line-height: 1;
    text-transform: uppercase; margin-top: -16px;
  }
  .wordmark__main { display: block; font-size: 78px; letter-spacing: 3px; }
  .wordmark__sub { display: block; font-size: 36px; letter-spacing: 6px; margin-top: 4px; }
  /* back */
  .card--back { font-family: 'Lato', sans-serif; color: var(--ink); }
  .identity {
    position: absolute; left: 96px; top: 120px; width: 210px; text-align: right;
  }
  .identity__name {
    font-family: 'Oswald', sans-serif; font-weight: 500;
    font-size: 34px; color: var(--accent); text-transform: uppercase;
    line-height: 1.05; letter-spacing: -.5px; white-space: nowrap;
  }
  .identity__role { font-size: 17px; margin-top: 2px; }
  .divider {
    position: absolute; left: 322px; top: 118px; width: 1px; height: 82px;
    background: var(--rule);
  }
  .contacts {
    position: absolute; left: 340px; top: 126px; list-style: none;
  }
  .contacts li {
    display: flex; align-items: center; gap: 9px;
    font-size: 17px; line-height: 25px; white-space: nowrap;
  }
  .contacts svg { width: 16px; height: 16px; flex: none; }
  .address {
    position: absolute; left: 96px; bottom: 44px; font-size: 17px; white-space: nowrap;
  }
</style>
</head>
<body>
<main class="sheet">
  <section class="card card--front" aria-label="Card front">
    <h1 class="wordmark">
      <span class="wordmark__main">Anvil</span>
      <span class="wordmark__sub">Mechanical</span>
    </h1>
    <div class="card__band"></div>
  </section>

  <section class="card card--back" aria-label="Card back">
    <div class="identity">
      <h2 class="identity__name">Daniel Harper</h2>
      <p class="identity__role">Managing Director</p>
    </div>
    <div class="divider"></div>
    <ul class="contacts">
      <li>
        <svg viewBox="0 0 24 24" aria-hidden="true"><path fill="var(--accent)" d="M6.6 10.8a15 15 0 0 0 6.6 6.6l2.2-2.2c.3-.3.7-.4 1-.2 1.1.4 2.3.6 3.6.6.6 0 1 .4 1 1V20c0 .6-.4 1-1 1C10.6 21 3 13.4 3 4c0-.6.4-1 1-1h3.5c.6 0 1 .4 1 1 0 1.3.2 2.5.6 3.6.1.3 0 .7-.2 1z"/></svg>
        044-987 650 321
      </li>
      <li>
        <svg viewBox="0 0 24 24" aria-hidden="true"><rect x="2" y="5" width="20" height="14" fill="var(--accent)"/><path d="M2 5l10 8 10-8" fill="none" stroke="var(--card)" stroke-width="2"/></svg>
        hello@anvilmech.com
      </li>
      <li>
        <svg viewBox="0 0 24 24" aria-hidden="true"><g fill="none" stroke="var(--accent)" stroke-width="2"><circle cx="12" cy="12" r="9"/><ellipse cx="12" cy="12" rx="4" ry="9"/><path d="M3 12h18M5 7h14M5 17h14"/></g></svg>
        www.anvilmech.com
      </li>
    </ul>
    <p class="address">18 Foundry Lane, Millbrook, 60214</p>
    <div class="card__band"></div>
  </section>
</main>
</body>
</html>
```